Harborlane Consultants LLC web site

Harborlane Consultants LLC is a consulting and recruiting firm that provides education, perspective, guidance, and assistance to financial advisors. Dennis Malbrook is the founder of this new firm and is the only employee at this time.
Please see the attached overview which will provide much narrative describing the firm, its purpose, scope of services offered, and other useful information to help you design a web site.

Target Market(s)

US based financial advisors who are looking to transition their business to an independent ( non-employee ) business model.

Industry/Entity Type

Consultant

Coding

Coded - Design and coding required

Number of Pages Required

5+ page

Font styles to use
Sans Serif

Requirements
Must have
• all relevant pages for a basic web site : Home, About, Services offered, Contact, Resources , etc.
Nice to have
• color scheme : see logo in the attached briefing document

```html
<!DOCTYPE html>
<html lang="en">
<head>
<meta charset="utf-8">
<title>Harborlane Consultants LLC</title>
<link rel="stylesheet" href="https://fonts.googleapis.com/css2?family=Cinzel:wght@500;600;700&family=Roboto:wght@400;500;700&display=swap">
<style>
:root{
  --navy:#0e4a86;
  --navy-dark:#0b3b6c;
  --band:#0f5a97;
  --ink:#1b1b1b;
  --muted:#555;
  --topbar:#666;
  --line:#e3e3e3;
  --grey-bg:#ececec;
  --footer:#0c0c0c;
  --white:#fff;
}
*{margin:0;padding:0;box-sizing:border-box}
html,body{width:1200px;height:4231px;overflow:hidden}
body{font-family:"Roboto",Arial,sans-serif;color:var(--ink);background:var(--white);position:relative}
.abs{position:absolute}
a{color:inherit;text-decoration:none}

/* top bar */
.topbar{position:absolute;left:0;top:0;width:1200px;height:36px;background:var(--topbar)}
.topbar .phone{position:absolute;left:806px;top:9px;color:#fff;font-size:15px;display:flex;align-items:center;gap:7px}
.topbar .quote{position:absolute;left:951px;top:3px;width:148px;height:30px;background:var(--navy);color:#fff;font-size:11px;font-weight:500;display:flex;align-items:center;justify-content:center}

/* nav */
.nav{position:absolute;left:0;top:36px;width:1200px;height:59px;background:#fff}
.brand{position:absolute;left:100px;top:12px;display:flex;align-items:center;gap:10px}
.brand .dot{width:34px;height:34px;border-radius:50%;background:var(--navy)}
.brand .name{font-family:"Cinzel",Georgia,serif;color:var(--navy);font-size:17px;font-weight:600;line-height:1.05;letter-spacing:1px}
.nav ul{list-style:none;position:absolute;top:22px;left:0;width:1200px}
.nav li{position:absolute;font-size:14.5px;font-weight:500;color:#111}
.nav li.active{color:var(--navy)}
.nav li.active::after{content:"";position:absolute;left:0;right:0;bottom:-6px;height:2px;background:var(--navy)}

/* hero */
.hero{position:absolute;left:0;top:95px;width:1200px;height:595px;background:radial-gradient(ellipse at 60% 55%,#4f7a9e 0%,#25507a 40%,#14365a 75%,#0c2442 100%)}
.hero h1{position:absolute;left:0;width:1200px;top:222px;text-align:center;font-family:"Cinzel",Georgia,serif;font-weight:500;color:#fff;font-size:47px;letter-spacing:1px}
.hero p{position:absolute;left:0;width:1200px;top:284px;text-align:center;color:#fff;font-size:22px}
.btn-pill{position:absolute;border-radius:30px;display:flex;align-items:center;justify-content:center;font-weight:500;font-size:15px}
.hero .cta{left:519px;top:334px;width:163px;height:40px;background:var(--navy);color:#fff}
.hero .dots{position:absolute;left:562px;top:557px;display:flex;gap:9px}
.hero .dots span{width:12px;height:12px;border-radius:50%;border:1.5px solid #fff}
.hero .dots span.on{background:#fff}

/* section titles */
.sec-title{position:absolute;left:0;width:1200px;text-align:center;font-family:"Cinzel",Georgia,serif;font-weight:600;font-size:34px;color:#111;letter-spacing:1px}
.sec-title::after{content:"";position:absolute;left:575px;width:50px;height:2px;background:var(--navy);bottom:-8px}

/* cards */
.card{position:absolute;background:#fff;border:1px solid var(--line)}
.card .ph{width:100%}
.card h3{font-size:15.5px;font-weight:500;line-height:1.45;margin:16px 13px 8px;text-transform:uppercase;color:#111}
.card p{font-size:12.5px;line-height:1.8;color:var(--muted);margin:0 13px}
.card .more{position:absolute;left:13px;font-size:13.5px;font-weight:700;color:var(--navy);display:flex;align-items:center;gap:6px}

/* about */
.about{position:absolute;left:0;top:1338px;width:1200px;height:496px;background:linear-gradient(90deg,#0f5190 0%,#135e9c 60%,#0f5593 100%)}
.about h2{position:absolute;left:607px;top:96px;font-family:"Cinzel",Georgia,serif;font-weight:500;font-size:38px;color:#fff}
.about p{position:absolute;left:607px;width:440px;font-size:13px;line-height:1.75;color:#fff}
.about .learn{left:607px;top:364px;width:158px;height:42px;border:1.5px solid #fff;color:#fff}

/* why */
.why h2{position:absolute;left:105px;top:1945px;font-family:"Cinzel",Georgia,serif;font-weight:600;font-size:37px;color:#111}
.why p{position:absolute;left:105px;width:450px;font-size:12.5px;line-height:1.82;color:var(--muted)}
.why .cta{left:101px;top:2270px;width:163px;height:40px;background:var(--navy);color:#fff}

/* provides */
.provides{position:absolute;left:0;top:2400px;width:1200px;height:497px;background:radial-gradient(ellipse at 30% 40%,#f4f4f4,#e6e6e6)}
.prov-label{position:absolute;font-size:18px;font-weight:500;color:#111;line-height:1.35}

/* blogs */
.card.blog h3{font-size:17px;font-weight:700;line-height:1.35;margin:16px 13px 8px;text-transform:none}
.blog .more{font-size:13px;text-decoration:underline}

/* schedule */
.schedule{position:absolute;left:0;top:3562px;width:1200px;height:332px;background:linear-gradient(180deg,#0d4e8c,#0f5a98)}
.schedule h2{position:absolute;left:0;width:1200px;top:92px;text-align:center;font-family:"Cinzel",Georgia,serif;font-weight:500;font-size:36px;line-height:1.22;color:#fff;letter-spacing:1px}
.schedule .cta{left:521px;top:200px;width:158px;height:42px;border:1.5px solid #fff;color:#fff}

/* footer */
.footer{position:absolute;left:0;top:3894px;width:1200px;height:337px;background:var(--footer);color:#fff}
.footer h4{position:absolute;font-family:"Cinzel",Georgia,serif;font-weight:500;font-size:15px;letter-spacing:1px}
.footer .fbrand{position:absolute;left:100px;top:80px;display:flex;align-items:center;gap:10px}
.footer .fbrand .dot{width:60px;height:60px;border-radius:50%;background:#fff}
.footer .fbrand .name{font-family:"Cinzel",Georgia,serif;font-size:21px;font-weight:500;line-height:1.1;letter-spacing:2px}
.footer .about-txt{position:absolute;left:100px;top:160px;width:260px;font-size:12.5px;line-height:1.8}
.footer ul{list-style:none;position:absolute;left:409px;top:80px;font-size:13.5px;line-height:28px}
.footer .contact{position:absolute;left:561px;top:80px;font-size:13.5px}
.footer .contact div{display:flex;align-items:center;gap:9px;height:37px}
.footer .news{position:absolute;left:848px;top:88px;width:252px;height:36px;display:flex}
.footer .news span{flex:1;background:#fff;color:#777;font-size:13px;padding:10px}
.footer .news b{width:40px;background:var(--navy);display:flex;align-items:center;justify-content:center}
.footer .social{position:absolute;left:851px;top:162px;font-size:13.5px;display:flex;align-items:center;gap:8px}
.footer .social i{width:11px;height:11px;border-radius:50%;background:#fff;display:inline-block}
.footer .copy{position:absolute;left:0;width:1200px;top:305px;text-align:center;font-size:13.5px}
</style>
</head>
<body>

<div class="topbar">
  <div class="phone">
    <svg width="13" height="13" viewBox="0 0 24 24"><path fill="#fff" d="M6.6 10.8a15.1 15.1 0 006.6 6.6l2.2-2.2c.3-.3.7-.4 1-.2 1.1.4 2.3.6 3.6.6.6 0 1 .4 1 1V20c0 .6-.4 1-1 1A17 17 0 013 4c0-.6.4-1 1-1h3.5c.6 0 1 .4 1 1 0 1.3.2 2.5.6 3.6.1.3 0 .7-.2 1z"/></svg>
    555-214-0387
  </div>
  <a class="quote" href="#">REQUEST A QUOTE</a>
</div>

<header class="nav">
  <div class="brand"><span class="dot"></span><span class="name">HARBORLANE<br>CONSULTANTS LLC</span></div>
  <ul>
    <li class="active" style="left:423px">HOME</li>
    <li style="left:537px">ABOUT</li>
    <li style="left:658px">SERVICES OFFERED</li>
    <li style="left:869px">CONTACT</li>
    <li style="left:1009px">RESOURCES</li>
  </ul>
</header>

<section class="hero" role="img" aria-label="Aerial photo of dark blue ocean waves breaking into white foam">
  <svg class="abs" style="left:66px;top:280px" width="20" height="36" viewBox="0 0 20 36"><path d="M17 2L3 18l14 16" fill="none" stroke="#fff" stroke-width="2"/></svg>
  <svg class="abs" style="left:1115px;top:280px" width="20" height="36" viewBox="0 0 20 36"><path d="M3 2l14 16L3 34" fill="none" stroke="#fff" stroke-width="2"/></svg>
  <h1>HARBORLANE CONSULTANTS LLC</h1>
  <p>helping financial advisors to navigate their journey to independence</p>
  <a class="btn-pill cta" href="#">GET STARTED</a>
  <div class="dots"><span class="on"></span><span></span><span></span><span></span></div>
</section>

<!-- services -->
<h2 class="sec-title" style="top:772px">SERVICES OFFERED</h2>
<svg class="abs" style="left:62px;top:1045px" width="18" height="32" viewBox="0 0 18 32"><path d="M15 2L3 16l12 14" fill="none" stroke="#333" stroke-width="1.8"/></svg>
<svg class="abs" style="left:1114px;top:1045px" width="18" height="32" viewBox="0 0 18 32"><path d="M3 2l12 14L3 30" fill="none" stroke="#333" stroke-width="1.8"/></svg>

<article class="card" style="left:99px;top:844px;width:325px;height:399px">
  <div class="ph" style="height:223px;background:linear-gradient(135deg,#9aa3ad,#4a5460 60%,#c7ccd2)" role="img" aria-label="Photo of two businessmen shaking hands in an office"></div>
  <h3>A fiduciary relationship for<br>your business</h3>
  <p>One very important thing to know about me and how i work with clients is that I will always put your interests first. That may sound intuitive</p>
  <a class="more" style="top:368px" href="#">LEARN MORE <svg width="18" height="10" viewBox="0 0 18 10"><path d="M0 5h16M12 1l4 4-4 4" fill="none" stroke="#0e4a86" stroke-width="1.4"/></svg></a>
</article>
<article class="card" style="left:437px;top:844px;width:325px;height:399px">
  <div class="ph" style="height:223px;background:linear-gradient(135deg,#d8d8d4,#8c8b86 55%,#4b4a47)" role="img" aria-label="Photo of a team of advisors meeting around a table with laptops"></div>
  <h3>Services for teams and advisors<br>in transition</h3>
  <p>Making any business transition is a complex undertaking . Harborlane Consultants offers a multi-step , comprehensive process</p>
  <a class="more" style="top:368px" href="#">LEARN MORE <svg width="18" height="10" viewBox="0 0 18 10"><path d="M0 5h16M12 1l4 4-4 4" fill="none" stroke="#0e4a86" stroke-width="1.4"/></svg></a>
</article>
<article class="card" style="left:775px;top:844px;width:325px;height:399px">
  <div class="ph" style="height:223px;background:linear-gradient(135deg,#5a6b80,#c8d0da 55%,#eef0f3)" role="img" aria-label="Photo of hands reviewing financial charts and a tablet on a desk"></div>
  <h3>Services for existing RIAs</h3>
  <p>Let's face it. You have a business to run. You have clients , and you have assets, both of which give you plenty to worry about. You have organic growth goals and are busy trying</p>
  <a class="more" style="top:368px" href="#">LEARN MORE <svg width="18" height="10" viewBox="0 0 18 10"><path d="M0 5h16M12 1l4 4-4 4" fill="none" stroke="#0e4a86" stroke-width="1.4"/></svg></a>
</article>

<!-- about -->
<section class="about">
  <div class="abs" style="left:181px;top:77px;width:344px;height:344px;border-radius:50%;background:radial-gradient(circle at 50% 40%,#7a7a7a,#3d3d3d)" role="img" aria-label="Portrait photo of founder Dennis Malbrook"></div>
  <h2>About Us</h2>
  <p style="top:158px">Harborlane Consultants LLC is a consulting and recruiting firm that provides education, perspective, guidance, and assistance to financial advisors. Specifically, we are focused on serving two distinct profiles of client :</p>
  <p style="top:234px">First, we assist financial advisors as they explore, plan, and execute their professional journey to independence. Most typically , this transition involves leaving the advisor's existing broker/dealer and either joining a new broker/dealer as an independent rep or establishing and launching a new and independent firm as a Registered Investment Advisor</p>
  <a class="btn-pill learn" href="#">LEARN MORE</a>
</section>

<!-- why -->
<section class="why">
  <h2>Why work with me ?</h2>
  <p style="top:2015px">In short, experience. I have spent my entire 35 year career in this industry, with the last 22 years spent in this exact endeavor... helping advisors like you to learn about, envision , and realize their dream of becoming independent advisors and business owners</p>
  <p style="top:2114px">My range of experience includes roles within many of the top companies in the financial services industry and includes positions in trading, institutional sales, retirement plan consulting, retail advisory, RIA custody sales, IBD regional management, executive director for business development (for a large strategic intermediary firm), and head of breakaway strategy for a large RIA custody provider.</p>
  <a class="btn-pill cta" href="#">GET STARTED</a>
  <svg class="abs" style="left:876px;top:1888px" width="220" height="230" viewBox="0 0 220 230">
    <defs><pattern id="dotgrid" width="11" height="11" patternUnits="userSpaceOnUse"><circle cx="2" cy="2" r="1.4" fill="#b9c2cc"/></pattern></defs>
    <rect width="220" height="230" fill="url(#dotgrid)"/>
  </svg>
  <div class="abs" style="left:616px;top:1921px;width:446px;height:387px;border-radius:6px;background:linear-gradient(180deg,#1e2a4a 0%,#4a4d6a 40%,#c7835a 72%,#3b2a22 100%)" role="img" aria-label="Photo of a striped lighthouse at sunset"></div>
</section>

<!-- provides -->
<section class="provides">
  <h2 class="sec-title" style="top:62px">WE PROVIDES</h2>
  <svg class="abs" style="left:0;top:0" width="1200" height="497" viewBox="0 0 1200 497">
    <g fill="none" stroke="#0e4a86" stroke-width="1.3">
      <path d="M421 167 H475 L517 220"/>
      <path d="M804 167 H750 L710 220"/>
      <path d="M421 387 H475 L517 337"/>
      <path d="M804 387 H750 L710 337"/>
    </g>
    <g fill="#0e4a86"><circle cx="517" cy="220" r="6"/><circle cx="710" cy="220" r="6"/><circle cx="517" cy="337" r="6"/><circle cx="710" cy="337" r="6"/></g>
    <circle cx="612" cy="281" r="120" fill="#fff" stroke="#0e4a86" stroke-width="3"/>
    <text x="612" y="287" text-anchor="middle" font-family="Cinzel, Georgia, serif" font-size="19" font-weight="600" fill="#0e4a86">HARBORLANE</text>
    <g fill="#fff" stroke="#0e4a86" stroke-width="2">
      <circle cx="383" cy="167" r="37"/><circle cx="842" cy="167" r="37"/>
      <circle cx="383" cy="387" r="37"/><circle cx="842" cy="387" r="37"/>
    </g>
    <g fill="#0e4a86"><polygon points="365,160 383,151 401,160 383,169"/><path d="M372 165v9c6 4 16 4 22 0v-9l-11 6z"/></g>
    <g fill="none" stroke="#0e4a86" stroke-width="2.2"><rect x="828" y="153" width="24" height="16"/><circle cx="836" cy="177" r="4"/><path d="M830 190c0-6 12-6 12 0M852 161l8 -6"/></g>
    <g fill="none" stroke="#0e4a86" stroke-width="2.2"><circle cx="383" cy="374" r="5"/><path d="M373 398l6-16h8l6 16M370 388h26"/></g>
    <g fill="none" stroke="#0e4a86" stroke-width="2.2"><circle cx="834" cy="382" r="5"/><path d="M824 402c0-8 20-8 20 0"/><rect x="846" y="370" width="10" height="10"/><path d="M848 402v-8M853 402v-12M858 402v-6"/></g>
  </svg>
  <div class="prov-label" style="left:229px;top:156px">EDUCATION</div>
  <div class="prov-label" style="left:893px;top:156px">GUIDANCE</div>
  <div class="prov-label" style="left:210px;top:375px">PERSPECTIVE</div>
  <div class="prov-label" style="left:893px;top:362px">FINANCIAL<br>ADVISORS</div>
</section>

<!-- blogs -->
<h2 class="sec-title" style="top:2980px">LATEST FROM BLOGS</h2>
<article class="card blog" style="left:100px;top:3058px;width:320px;height:409px">
  <div class="ph" style="height:208px;background:linear-gradient(135deg,#8c7a55,#d9d4c9 50%,#5b5f66)" role="img" aria-label="Photo of a laptop and tablet on a desk"></div>
  <h3>The standard Lorem Ipsum passfe, used since the 1500s</h3>
  <p>Lorem ipsum dolor sit amet, consectetur adipiscing elit, sed do eiusmod tempor incididunt ut labore et dolore magna aliqua. Quis ipsum suspisse ultrices gravida.</p>
  <a class="more" style="top:374px" href="#">LEARN MORE &raquo;</a>
</article>
<article class="card blog" style="left:440px;top:3058px;width:320px;height:409px">
  <div class="ph" style="height:208px;background:linear-gradient(135deg,#1b2a44,#4d6b93 55%,#c98a4a)" role="img" aria-label="Photo of a glowing stock chart above a tablet"></div>
  <h3>The standard Lorem Ipsum passfe, used since the 1500s</h3>
  <p>Lorem ipsum dolor sit amet, consectetur adipiscing elit, sed do eiusmod tempor incididunt ut labore et dolore magna aliqua. Quis ipsum suspisse ultrices gravida.</p>
  <a class="more" style="top:374px" href="#">LEARN MORE &raquo;</a>
</article>
<article class="card blog" style="left:780px;top:3058px;width:320px;height:409px">
  <div class="ph" style="height:208px;background:linear-gradient(135deg,#2f6f9a,#7fb3c8 50%,#1c3550)" role="img" aria-label="Photo of a businessman before a city skyline with a rising arrow"></div>
  <h3>The standard Lorem Ipsum passfe, used since the 1500s</h3>
  <p>Lorem ipsum dolor sit amet, consectetur adipiscing elit, sed do eiusmod tempor incididunt ut labore et dolore magna aliqua. Quis ipsum suspisse ultrices gravida.</p>
  <a class="more" style="top:374px" href="#">LEARN MORE &raquo;</a>
</article>

<!-- schedule -->
<section class="schedule">
  <h2>Schedule an exploratory<br>meeting now</h2>
  <a class="btn-pill cta" href="#">CONTACT US</a>
</section>

<!-- footer -->
<footer class="footer">
  <div class="fbrand"><span class="dot"></span><span class="name">HARBORLANE<br>CONSULTANTS LLC</span></div>
  <p class="about-txt">Harborlane Consultants LLC is a consulting &amp; recruiting firm that provides education, perspective, guidance, and assistance to financial advisors.</p>
  <h4 style="left:409px;top:73px">QUICK LINKS</h4>
  <ul style="top:100px"><li>Home</li><li>About</li><li>Services Offered</li><li>Contact</li><li>Resources</li></ul>
  <h4 style="left:561px;top:73px">CONTACT US</h4>
  <div class="contact" style="top:96px">
    <div><svg width="13" height="16" viewBox="0 0 12 16"><path fill="#fff" d="M6 0a6 6 0 00-6 6c0 4.5 6 10 6 10s6-5.5 6-10a6 6 0 00-6-6zm0 8.5A2.5 2.5 0 116 3.5a2.5 2.5 0 010 5z"/></svg>Cedar Bay, FL</div>
    <div><svg width="14" height="14" viewBox="0 0 24 24"><path fill="#fff" d="M6.6 10.8a15.1 15.1 0 006.6 6.6l2.2-2.2c.3-.3.7-.4 1-.2 1.1.4 2.3.6 3.6.6.6 0 1 .4 1 1V20c0 .6-.4 1-1 1A17 17 0 013 4c0-.6.4-1 1-1h3.5c.6 0 1 .4 1 1 0 1.3.2 2.5.6 3.6.1.3 0 .7-.2 1z"/></svg>555-214-0387</div>
    <div><svg width="15" height="11" viewBox="0 0 16 12"><rect x="0.7" y="0.7" width="14.6" height="10.6" fill="none" stroke="#fff" stroke-width="1.4"/><path d="M1 1l7 6 7-6" fill="none" stroke="#fff" stroke-width="1.4"/></svg>hello@harborlane-consultants.com</div>
  </div>
  <h4 style="left:852px;top:73px">SUBSCRIBE OUR NEWSLETTER</h4>
  <div class="news" style="top:110px"><span>Email</span><b><svg width="15" height="15" viewBox="0 0 16 16"><path fill="#fff" d="M15 1L1 7l5 2 2 5z"/></svg></b></div>
  <div class="social">Social Community- <i></i><i></i><i></i><i></i></div>
  <p class="copy">Copyright &copy; 2021 Harborlane Consultants LLC. All rights reserved.</p>
</footer>

</body>
</html>
```